Business card design for Automotive workshop

We need a business card for a new automotive repair and tyre shop called Ridgeback Prime Automotive located in New Zealand. We are a clean, modern and fresh workshop and company.

Front needs to feature logo,
my name:
Lachie Westergaard (director)

Address:
48 Marlow Lane
Tawhiri Bay 3596

Phone: 07 842 1937
Mobile: 027 519 2764
Email: office@ridgebackmotors.co.nz
Website: ridgebackmotors.co.nz

Back needs to feature an area to write down appointment details, date and time.

Also feature a list of jobs and work we do such as,
Vehicle Servicing
All Mechanical Repairs
Warrant of Fitness
Tyres & Wheel Alignments
Automotive Diagnostics
Automotive Parts & Supplies

```html
<!DOCTYPE html>
<html lang="en">
<head>
<meta charset="utf-8">
<title>Ridgeback Prime Automotive — Business Card</title>
<link rel="stylesheet" href="https://fonts.googleapis.com/css2?family=Ubuntu:wght@500;700&family=Open+Sans:wght@400&display=swap">
<style>
  :root {
    --backdrop: #cdbdbd;
    --card-dark: #000000;
    --card-light: #f7f7f7;
    --brand-red: #c1181f;
    --ink-light: #ffffff;
    --ink-dark: #1b1b1b;
  }
  * { margin: 0; padding: 0; box-sizing: border-box; }
  html, body { width: 1200px; height: 1200px; overflow: hidden; }
  body { background: var(--backdrop); position: relative; font-family: "Open Sans", sans-serif; }

  .card { position: absolute; left: 250px; width: 700px; height: 400px; }
  .card--front { top: 147px; background: var(--card-dark); color: var(--ink-light); }
  .card--back { top: 652px; background: linear-gradient(135deg, #ffffff 0%, var(--card-light) 55%, #e9e9e9 100%); color: var(--ink-dark); }

  .brand-name {
    position: absolute; left: 0; right: 0; text-align: center;
    font-family: "Ubuntu", sans-serif; font-weight: 700;
    font-size: 31px; letter-spacing: 1px; text-transform: uppercase;
    color: var(--brand-red); white-space: nowrap;
  }
  .card--front .brand-name { top: 62px; }
  .card--back .brand-name { top: 46px; }

  .identity { position: absolute; right: 395px; top: 218px; text-align: right; font-family: "Ubuntu", sans-serif; font-weight: 700; }
  .identity__name { font-size: 27px; color: var(--brand-red); line-height: 34px; }
  .identity__role { font-size: 20px; line-height: 28px; }
  .identity__address { margin-top: 24px; font-size: 21px; line-height: 28px; }

  .divider { position: absolute; left: 330px; top: 208px; width: 2px; height: 166px; background: var(--ink-light); }

  .contact-list { position: absolute; left: 348px; top: 0; list-style: none; }
  .contact-item { position: absolute; left: 0; display: flex; align-items: center; white-space: nowrap; }
  .contact-item svg { width: 24px; height: 24px; flex: none; }
  .contact-item span { margin-left: 11px; }
  .contact-item--phone { top: 222px; font-size: 21px; }
  .contact-item--mobile { top: 263px; font-size: 21px; }
  .contact-item--email { top: 305px; font-size: 18px; }
  .contact-item--web { top: 339px; font-size: 18px; }

  .appointment { position: absolute; left: 39px; top: 140px; width: 600px; }
  .appointment__title { font-size: 30px; line-height: 40px; color: #2a2a2a; }
  .appointment__field { display: flex; align-items: baseline; font-size: 24px; line-height: 32px; margin-top: 19px; }
  .appointment__field:first-of-type { margin-top: 24px; }
  .appointment__field .fill-line { flex: 1; margin-left: 8px; border-bottom: 2px dotted #333; height: 2px; transform: translateY(-4px); }

  .services { position: absolute; top: 340px; left: 0; right: 0; }
  .services__column {
    position: absolute; top: 0; transform: translateX(-50%); text-align: center;
    font-family: "Ubuntu", sans-serif; font-weight: 700; font-size: 17px; line-height: 21px;
    color: var(--brand-red); white-space: nowrap; list-style: none;
  }
  .services__column--a { left: 128px; }
  .services__column--b { left: 340px; }
  .services__column--c { left: 563px; }
</style>
</head>
<body>

<section class="card card--front" aria-label="Business card front">
  <div class="brand-name">Ridgeback Prime Automotive</div>

  <div class="identity">
    <div class="identity__name">Lachie Westergaard</div>
    <div class="identity__role">director</div>
    <div class="identity__address">48 Marlow Lane<br>Tawhiri Bay 3596</div>
  </div>

  <div class="divider"></div>

  <ul class="contact-list">
    <li class="contact-item contact-item--phone">
      <svg viewBox="0 0 24 24" aria-hidden="true"><path d="M6.6 3.5l3 3.2-1.8 2.2c1 2.3 2.9 4.3 5.3 5.4l2.2-1.8 3.2 3-1.6 3c-7 -.4-12.7-6.3-13.2-13.3z" fill="none" stroke="var(--brand-red)" stroke-width="2" stroke-linejoin="round"/><path d="M14 4a6 6 0 0 1 6 6M14 7.5a2.5 2.5 0 0 1 2.5 2.5" fill="none" stroke="var(--brand-red)" stroke-width="1.8" stroke-linecap="round"/></svg>
      <span>07 842 1937</span>
    </li>
    <li class="contact-item contact-item--mobile">
      <svg viewBox="0 0 24 24" aria-hidden="true"><rect x="6" y="2" width="12" height="20" rx="2" fill="none" stroke="var(--brand-red)" stroke-width="2"/><circle cx="12" cy="19" r="1" fill="var(--brand-red)"/></svg>
      <span>027 519 2764</span>
    </li>
    <li class="contact-item contact-item--email">
      <svg viewBox="0 0 24 24" aria-hidden="true"><rect x="2" y="5" width="20" height="14" fill="var(--brand-red)"/><path d="M2 5l10 8 10-8M2 19l8-7M22 19l-8-7" fill="none" stroke="#000" stroke-width="1.2"/></svg>
      <span>office@ridgebackmotors.co.nz</span>
    </li>
    <li class="contact-item contact-item--web">
      <svg viewBox="0 0 24 24" aria-hidden="true"><g fill="none" stroke="var(--brand-red)" stroke-width="1.4"><circle cx="12" cy="12" r="9.5"/><ellipse cx="12" cy="12" rx="4" ry="9.5"/><path d="M2.5 12h19M4 7h16M4 17h16"/></g></svg>
      <span>ridgebackmotors.co.nz</span>
    </li>
  </ul>
</section>

<section class="card card--back" aria-label="Business card back">
  <div class="brand-name">Ridgeback Prime Automotive</div>

  <div class="appointment">
    <div class="appointment__title">Appointment details</div>
    <div class="appointment__field">Date:<span class="fill-line"></span></div>
    <div class="appointment__field">Time:<span class="fill-line"></span></div>
  </div>

  <div class="services">
    <ul class="services__column services__column--a">
      <li>Vehicle Servicing</li>
      <li>Tyres &amp; Wheel Alignments</li>
    </ul>
    <ul class="services__column services__column--b">
      <li>All Mechanical Repairs</li>
      <li>Automotive Diagnostic</li>
    </ul>
    <ul class="services__column services__column--c">
      <li>Warrant of Fitness</li>
      <li>Automotive Parts &amp; Supplies</li>
    </ul>
  </div>
</section>

</body>
</html>
```